R & M Holdings of Fairhaven, LLC
“TRUST is the CORE of EVERY HOME"
R & M Holdings of Fairhaven, LLC -
Creative Brief
Professional
Bertram Lasko
Property Manager
P.O. Box 38216 Brookmere, OR 97534
rmholdings2011@quillpost.example

```html
<!DOCTYPE html>
<html lang="en">
<head>
<meta charset="utf-8">
<title>R &amp; M Holdings of Fairhaven, LLC — Business Cards</title>
<link rel="stylesheet" href="https://fonts.googleapis.com/css2?family=Arimo:wght@400;700&display=swap">
<style>
  :root{
    --bg:#e9e9e9;
    --white:#ffffff;
    --black:#0c0c10;
    --blue:#1c6fc4;
    --blue-deep:#0e3f8c;
    --blue-light:#3ea2e6;
    --gold:#f2b705;
    --ink:#1d2b3a;
    --muted:#4a5563;
    --on-dark:#ffffff;
  }
  *{box-sizing:border-box;margin:0;padding:0}
  html,body{width:1200px;height:847px;overflow:hidden}
  body{background:var(--bg);font-family:"Arimo",Arial,sans-serif;position:relative}
  .card{position:absolute;width:520px;height:300px;border-radius:14px;overflow:hidden;
        box-shadow:0 6px 18px rgba(0,0,0,.18)}
  .card--front{left:50px;top:274px;background:var(--white)}
  .card--back{left:630px;top:274px;background:var(--black)}
  .card__waves{position:absolute;inset:0;width:100%;height:100%}
  .brand{position:absolute;left:0;right:0;top:44px;text-align:center}
  .brand__name{display:inline-flex;align-items:center;gap:10px;font-weight:700;font-size:21px;letter-spacing:.5px;color:var(--blue-deep)}
  .brand__mark{width:14px;height:14px;background:var(--gold)}
  .brand__tagline{margin-top:12px;font-size:12px;font-weight:700;letter-spacing:1.6px;color:var(--blue-deep)}
  .card--back .brand__name{color:var(--on-dark)}
  .card--back .brand__tagline{color:var(--gold)}
  .person{position:absolute;left:40px;top:176px}
  .person__name{font-size:14px;font-weight:700;color:var(--ink)}
  .person__role{font-size:10px;color:var(--muted);margin-top:3px}
  .card--back .person{top:128px}
  .card--back .person__name{color:var(--on-dark)}
  .card--back .person__role{color:#c8d0da}
  .contact{position:absolute;right:30px;top:190px;text-align:right;color:var(--on-dark);font-size:10px;line-height:1.45}
  .contact p.gap{margin-top:8px}
  .card--back .contact{top:150px}
</style>
</head>
<body>

<section class="card card--front" aria-label="Business card front">
  <svg class="card__waves" viewBox="0 0 520 300" preserveAspectRatio="none" aria-hidden="true">
    <defs>
      <linearGradient id="blueFront" x1="0" y1="0" x2="1" y2="1">
        <stop offset="0" stop-color="#3ea2e6"/>
        <stop offset="1" stop-color="#0e3f8c"/>
      </linearGradient>
    </defs>
    <path d="M0 0 L40 0 C20 40 10 80 0 110 Z" fill="var(--blue)"/>
    <path d="M0 240 C150 275 300 140 520 150 L520 300 L0 300 Z" fill="url(#blueFront)"/>
    <path d="M0 228 C150 262 300 126 520 136 L520 146 C300 136 150 272 0 238 Z" fill="var(--gold)"/>
  </svg>
  <div class="brand">
    <div class="brand__name"><span class="brand__mark"></span>R &amp; M Holdings of Fairhaven, LLC</div>
    <div class="brand__tagline">TRUST is the CORE of EVERY HOME</div>
  </div>
  <div class="person">
    <p class="person__name">Bertram Lasko</p>
    <p class="person__role">Property Manager</p>
  </div>
  <div class="contact">
    <p>P.O. Box 38216</p>
    <p>Brookmere, OR 97534</p>
    <p class="gap">Phone: (555) 410-2736 | (555) 418-9051</p>
    <p>Fax: (555) 410-2748</p>
    <p class="gap">Email: rmholdings2011@quillpost.example</p>
  </div>
</section>

<section class="card card--back" aria-label="Business card back">
  <svg class="card__waves" viewBox="0 0 520 300" preserveAspectRatio="none" aria-hidden="true">
    <defs>
      <linearGradient id="blueBack" x1="0" y1="0" x2="1" y2="1">
        <stop offset="0" stop-color="#1c6fc4"/>
        <stop offset="1" stop-color="#0e3f8c"/>
      </linearGradient>
      <radialGradient id="glow" cx=".5" cy=".25" r=".5">
        <stop offset="0" stop-color="#2a3a55"/>
        <stop offset="1" stop-color="#0c0c10"/>
      </radialGradient>
    </defs>
    <rect width="520" height="300" fill="url(#glow)"/>
    <path d="M0 200 C150 240 300 100 520 110 L520 300 L0 300 Z" fill="url(#blueBack)"/>
    <path d="M0 188 C150 226 300 86 520 96 L520 106 C300 96 150 236 0 198 Z" fill="var(--gold)"/>
  </svg>
  <div class="brand">
    <div class="brand__name"><span class="brand__mark"></span>R &amp; M Holdings of Fairhaven, LLC</div>
    <div class="brand__tagline">TRUST is the CORE of EVERY HOME</div>
  </div>
  <div class="person">
    <p class="person__name">Bertram Lasko</p>
    <p class="person__role">Property Manager</p>
  </div>
  <div class="contact">
    <p>P.O. Box 38216</p>
    <p>Brookmere, OR 97534</p>
    <p class="gap">Phone: (555) 410-2736 | (555) 418-9051</p>
    <p>Fax: (555) 410-2748</p>
    <p class="gap">Email: rmholdings2011@quillpost.example</p>
  </div>
</section>

</body>
</html>
```